Visitenkarten-Design für Erfindung & Entwicklung von Produkten für Körper, Geist und Seele
Zielgruppe
Erfindung und Entwicklung von Produkten für Körper Geist und Seele
Als grosser Überbegriff Produkte zur Regenration und Wohlbefinden sowie Bewusstseins Förderung
' Beispiel ' www. o-senva.ch
Zielgruppe Jedermann und Jedefrau die Ihr Bewusstein für Ihre Gesundheit und Heilung auf allen Ebenen vertiefen möchte ....
Aufgabenstellung
Das Logo ist Entwickelt in einem Entwurfsstadium kleine Verbesserungsvorschläge wären möglich
Vorallem geht es um das Layout und der sauberen Daten Erfassung
sowie die Gestaltung der Visitenkarte

```html
<!DOCTYPE html>
<html lang="de">
<head>
<meta charset="utf-8">
<title>osenva – Visitenkarte</title>
<link href="https://fonts.googleapis.com/css2?family=Open+Sans:wght@400;600&display=swap" rel="stylesheet">
<style>
  :root {
    --stage: #2b2b2b;
    --card: #ffffff;
    --green: #3f7a2a;
    --ink: #2a2a2a;
    --rule: #555555;
    --pattern-a: #e9ede0;
    --pattern-b: #dfe6d6;
  }
  * { box-sizing: border-box; margin: 0; padding: 0; }
  html, body { width: 1200px; height: 901px; overflow: hidden; }
  body {
    background: var(--stage);
    font-family: "Open Sans", Arial, sans-serif;
    color: var(--ink);
    display: flex;
    align-items: center;
    justify-content: center;
    gap: 40px;
  }
  .card {
    position: relative;
    width: 520px;
    height: 305px;
    background: var(--card);
    overflow: hidden;
  }

  /* front */
  .brand {
    position: absolute;
    left: 40px;
    top: 90px;
    display: flex;
    align-items: center;
    gap: 10px;
  }
  .brand-mark {
    width: 22px; height: 22px;
    background: var(--green);
    flex: none;
  }
  .brand-name {
    font-weight: 400;
    font-size: 26px;
    line-height: 1;
    color: var(--ink);
  }
  .divider {
    position: absolute;
    left: 232px; right: 32px; top: 150px;
    height: 1px;
    background: var(--rule);
  }
  .address {
    position: absolute;
    right: 32px; top: 100px;
    text-align: right;
    font-style: normal;
    font-size: 12px;
    line-height: 1.45;
  }
  .person {
    position: absolute;
    left: 40px; bottom: 30px;
  }
  .person-name {
    color: var(--green);
    font-weight: 600;
    font-size: 17px;
    letter-spacing: .5px;
  }
  .person-role { font-size: 12.5px; margin-bottom: 4px; }
  .contact {
    list-style: none;
    font-size: 12.5px;
    line-height: 1.5;
  }
  .contact li { display: flex; align-items: center; gap: 7px; }
  .contact svg { width: 11px; height: 11px; fill: var(--green); flex: none; }

  /* back */
  .pattern {
    position: absolute; inset: 0;
    background: linear-gradient(135deg, var(--pattern-a), var(--pattern-b));
  }
  .card-back .brand { left: 110px; top: 130px; gap: 14px; }
  .card-back .brand-mark { width: 40px; height: 40px; }
  .card-back .brand-name { font-size: 40px; }
</style>
</head>
<body>

  <section class="card card-front">
    <div class="brand">
      <span class="brand-mark"></span>
      <span class="brand-name">osenva</span>
    </div>
    <div class="divider"></div>
    <address class="address">Mirelweg 14<br>8329 TALMATT</address>

    <div class="person">
      <p class="person-name">KOLU TRISVEND</p>
      <p class="person-role">Geschäftsführer</p>
      <ul class="contact">
        <li>
          <svg viewBox="0 0 24 24"><path d="M6.6 10.8a15 15 0 0 0 6.6 6.6l2.2-2.2a1 1 0 0 1 1-.25 11.4 11.4 0 0 0 3.6.57 1 1 0 0 1 1 1V20a1 1 0 0 1-1 1A17 17 0 0 1 3 4a1 1 0 0 1 1-1h3.5a1 1 0 0 1 1 1c0 1.25.2 2.45.57 3.57a1 1 0 0 1-.25 1z"/></svg>
          079 000 12 34
        </li>
        <li>
          <svg viewBox="0 0 24 24"><path d="M2 5h20v14H2z M2 5l10 7 10-7" stroke="#fff" stroke-width="1.5"/></svg>
          kolu.trisvend@o-senva.ch
        </li>
        <li>
          <svg viewBox="0 0 24 24"><circle cx="12" cy="12" r="10"/><path d="M2 12h20M12 2c3 3 3 17 0 20M12 2c-3 3-3 17 0 20" stroke="#fff" stroke-width="1.3" fill="none"/></svg>
          www.o-senva.ch
        </li>
      </ul>
    </div>
  </section>

  <section class="card card-back">
    <div class="pattern" role="img" aria-label="Zartes Blattmuster in hellem Grün und Creme als Hintergrund"></div>
    <div class="brand">
      <span class="brand-mark"></span>
      <span class="brand-name">osenva</span>
    </div>
  </section>

</body>
</html>
```